Web Design (Coded) and Project - Finance Company

Corvale Lending Group is a mortgage broker company based in Sydney Australia and provides lending solutions for individuals and businesses.

Our target market is anyone with the financial means to get a loan.

I am looking for a website design in this contest. The site needs to be able to be viewed on a portable device such as Tabra, Fonix, etc.

I have the logo design and files which need to be used. I also have the NLBC logo which will need to be in the footer of each page.

The website needs to represent a big finance company with integrity and knowledge.

The website will need to be uploaded to Hostwillow.example.au as they are the hosting provider. I will also need the ability to make changes to the text and pictures in the future and upload the revisions. I need the website ready to go and ready to be uploaded onto Host Willow.

The website will consist of 6 pages in total There are 4 main pages that will be viewed and then 2 with Privacy and Internal Dispute Resolution which are only accessed through links. These will be as follows:

Home
I would prefer to have a fresh bright and professional looking home page given that most mortgage broker websites look the same with the menu buttons at the top.

Services
Details the loan types that we handle and some text for each one.

About Us
I have the text for this.

Contact Us
Form to have the following inputs:
• Surname
• First Name
• Suburb
• State
• Phone number
• Mobile number
• Email address
• Preferred contact
o Phone
o Mobile
o Email
• Reason for Enquiry
o First home buyer
o Refinance
o Investment Property
o Commercial lending
o Personal loan
o Other
• Comments

Privacy
This page will only be accessed from a link at the bottom of each page. I have the wording that I will provide.

Dispute Resolution Policy
This page will only be accessed from a link on the Contact Us page. I have the wording that I will provide.
Updates

The designs that are coming through so far are generally looking the same generic website layout. I am looking for the home page to be something different with more of a wow factor and something different to the standard page link menu accross the top of the screen. The content should be fairly minimal given that I am a new business there will be limited text for each page. I am happy to increase the budget if required as I appreciate there will be more work involved.

Reason: I am extending the deadline as the design so far are good but fairly generic and template style home pages. For the home page I am looking for something a little more striking with a visual impact.

I have increased the payment by $200 to encourage more designs. Designs need to be relevant to the business, the number of pages and content. Several designs have come through looking good but just look like a standard template with my logo added, but the content does not match the business.

The brief stated that I am looking for the home page to be something different with more of a wow factor and something different to the standard page link menu accross the top of the screen. All of the designs have come through with the navigation bar along the top and a generic layout. I have attached a couple of idea's. Obviously these do not relate to the finance and mortgage industry but you can see the sort of style that gives the site a wow factor. The other pages can be more generic, but the first page is the attention grabber. You can also see the Fonix view that I am after. These are just templates from Host Willow that I could use to build the site, I just don't have the time or creative flair. Please submit more designs. Thanks for your work to date, Rob.

Hi. Could you please submit designs based on brief and the two screen shots attached. Mobile device view should work as per screen shots. Thanks, Rob

Reason: Still looking for designs to meet the brief provided.

Industry/Entity Type

Financial

Requirements
Must have
• Colour palette to be as supplied. I will post this shortly.
Should not have
• No cheesy smiley faces
No handshaking
No money pictures
No pictures of stones
No picture of people in an office looking at things
No lime green or purple in colour
Would prefer not to have a picture of the Quayline Span or Tidewater Hall

```html
<!DOCTYPE html>
<html lang="en">
<head>
<meta charset="utf-8">
<title>Services – Corvale Lending Group</title>
<link rel="stylesheet" href="https://fonts.googleapis.com/css2?family=Source+Sans+3:wght@400;700&family=Roboto+Condensed:wght@700&family=Arimo:wght@400;700&display=swap">
<style>
  :root {
    --page-bg: #f4f4f4;
    --sidebar-top: #1f1f1f;
    --sidebar-bottom: #0b0b0b;
    --header-bg: #1d1d1d;
    --accent: #1aa3e8;
    --accent-deep: #0a6fae;
    --nav-text: #ffffff;
    --body-text: #1f1f1f;
    --watermark: #a9a9a9;
  }
  * { margin: 0; padding: 0; box-sizing: border-box; }
  html, body { width: 1200px; height: 649px; overflow: hidden; background: var(--page-bg); }
  .page { position: relative; width: 1200px; height: 649px; background: var(--page-bg); }

  .sidebar {
    position: absolute; left: 0; top: 0; width: 245px; height: 649px;
    background: linear-gradient(180deg, var(--sidebar-top), var(--sidebar-bottom));
    border-right: 3px solid var(--accent);
    box-shadow: 3px 0 6px rgba(0,0,0,0.25);
  }
  .brand {
    height: 104px; background: var(--header-bg);
    border-bottom: 3px solid var(--accent);
    display: flex; align-items: center; gap: 10px; padding-left: 34px;
  }
  .brand-dot { width: 34px; height: 34px; border-radius: 50%; background: var(--accent); flex: none; }
  .brand-name {
    font-family: "Arimo", Arial, sans-serif; font-weight: 700; font-size: 17px;
    line-height: 18px; color: var(--nav-text); text-transform: uppercase; width: 150px;
  }

  .main-nav { position: absolute; top: 173px; left: 0; width: 245px; }
  .main-nav a {
    position: relative; display: block; height: 40px; line-height: 40px;
    padding-left: 35px; margin-bottom: 25px;
    font-family: "Arimo", Arial, sans-serif; font-size: 15px;
    color: var(--nav-text); text-decoration: none;
  }
  .main-nav .nav-marker { position: absolute; left: 0; top: 0; z-index: 0; }
  .main-nav .nav-label { position: relative; z-index: 1; }

  .legal {
    position: absolute; left: 35px; top: 595px;
    font-family: "Arimo", Arial, sans-serif; font-size: 8px; line-height: 16px;
    color: var(--nav-text);
  }
  .legal a { color: var(--nav-text); text-decoration: none; display: block; }

  .section-title {
    position: absolute; left: 243px; top: 78px; height: 450px; width: 80px;
    writing-mode: vertical-rl; transform: rotate(180deg);
    font-family: "Roboto Condensed", "Arial Narrow", sans-serif; font-weight: 700;
    font-size: 101px; line-height: 80px; letter-spacing: 1px;
    color: var(--watermark); text-align: center;
  }

  .content {
    position: absolute; left: 374px; top: 42px; width: 756px;
    font-family: "Source Sans 3", "Myriad Pro", sans-serif; font-size: 11.4px;
    line-height: 23px; color: var(--body-text);
  }
  .loan-type h2 { font-size: 11.4px; font-weight: 700; line-height: 23px; }
  .loan-type p { margin-bottom: 23px; }
</style>
</head>
<body>
<div class="page">
  <aside class="sidebar">
    <div class="brand">
      <span class="brand-dot"></span>
      <span class="brand-name">Corvale Lending Group</span>
    </div>

    <nav class="main-nav">
      <a href="#" class="is-active">
        <svg class="nav-marker" width="182" height="40" viewBox="0 0 182 40" aria-hidden="true">
          <defs>
            <linearGradient id="markerFill" x1="0" y1="0" x2="0" y2="1">
              <stop offset="0" stop-color="#27b4f2"/>
              <stop offset="1" stop-color="#0a6fae"/>
            </linearGradient>
          </defs>
          <polygon points="0,0.5 160,0.5 180.5,20 160,39.5 0,39.5" fill="url(#markerFill)" stroke="#5cc8f5" stroke-width="1"/>
        </svg>
        <span class="nav-label">Home</span>
      </a>
      <a href="#"><span class="nav-label">Services</span></a>
      <a href="#"><span class="nav-label">About Us</span></a>
      <a href="#"><span class="nav-label">Contact Us</span></a>
    </nav>

    <div class="legal">
      <a href="#">Privacy Policy</a>
      <span>© Corvale Lending Group</span>
    </div>
  </aside>

  <h1 class="section-title">SERVICES</h1>

  <main class="content">
    <section class="loan-type">
      <h2>Loan Type 1</h2>
      <p>Mauris ut dapibus justo. Integer sit amet pellentesque elit. Praesent volutpat, dolor ac sollicitudin venenatis, dui arcu mattis leo, non consequat tortor magna sed sapien. Etiam tempor feugiat mi, et egestas nibh hendrerit a. Lorem ipsum dolor sit amet, consectetur adipiscing elit. Morbi mauris magna, condimentum vitae imperdiet quis, malesuada at nulla. Donec vestibulum enim quis arcu accumsan sit amet pretium nunc blandit. Morbi tempus laoreet justo, eu venenatis sem tristique a. Mauris augue dolor, ullamcorper ac mollis in, tempor blandit arcu. In ullamcorper laoreet blandit. Nunc ullamcorper, erat at eleifend vulputate, lectus lacus vestibulum ipsum, sed interdum leo nunc quis lorem. Sed lacinia metus sed quam malesuada cursus. Ut at mi dolor. Suspendisse potenti. Donec volutpat sem id tellus ornare vel dapibus urna vestibulum. Morbi vehicula lobortis mauris et mattis.</p>
    </section>

    <section class="loan-type">
      <h2>Loan Type 2</h2>
      <p>Integer tempus malesuada lobortis. Pellentesque ut eleifend velit. Duis quis mauris metus, quis pharetra lectus. Nulla pretium, tortor in porta mattis, purus libero tincidunt ligula, vitae rutrum magna ipsum quis sapien. In hendrerit neque non sem rutrum sodales. In rhoncus urna eget leo porttitor malesuada. Mauris quis sem at ligula dignissim facilisis eu luctus risus.</p>
      <p>Morbi condimentum dictum bibendum. Quisque quis eleifend justo. Duis nisi ante, tristique eget feugiat non, faucibus eget risus. Aenean condimentum cursus eros, et lacinia diam semper id. Sed eget viverra neque. Sed eget faucibus justo. Donec sit amet lectus ligula, id vestibulum quam. Suspendisse at ligula felis. Suspendisse euismod quam sed nulla posuere sit amet lobortis metus elementum. Praesent ac lobortis est. Praesent purus metus, euismod vel scelerisque pulvinar, adipiscing nec nunc. Vivamus pulvinar lacus et lacus volutpat non sagittis felis volutpat. Class aptent taciti sociosqu ad litora torquent per conubia nostra, per inceptos himenaeos.</p>
    </section>

    <section class="loan-type">
      <h2>Loan Type 3</h2>
      <p>Maecenas imperdiet leo elit, at porta dui. Nullam elementum fermentum consequat. Nullam consectetur lorem id lacus iaculis tincidunt. Aliquam eu metus sem, a consequat est. Donec vel mi dolor, id imperdiet nunc. Etiam eget sem lacus. Quisque et ipsum tortor. Ut tempus ultrices magna, vel volutpat dui aliquam a. Sed nec diam est. Vestibulum mollis ultrices arcu, eu scelerisque arcu ornare nec. Nullam ultricies, urna eget commodo aliquam, ante augue consectetur augue, sit amet ornare risus arcu sit amet nisi.</p>
    </section>
  </main>
</div>
</body>
</html>
```